Minimalist, Flat(Matte) design for a Beef Jerky packaging company. No bullshit company looking for a

Need a packaging design for a new Beef Jerky product(in English). The name of the company is 'Velmor' and thus the packaging should reflect the bullish, tough, and simple nature of the beef jerky product. The finished product should communicate simplicity, minimalism, yet toughness and strength.

The logo should be simple, with a minimal number of colors , and should be either all white/cream, or have some red as well. Main colors should be white, cream, tinted red, and matte black. I think 4 colors max would be best. The closest example to an existing package style would be Korvanti Dusk clove cigarettes( image attached).

It will be on a matte black standing pouch package. See image for package type. Package dimensions:

Dimension: Width x Gusset x Height
INCH : 5.125" (W) x 3.125" (G) x 8.125" (H)
MILLIMETER : 130mm (W) x 80mm (G) x 205mm (H)

I don't have anything totally specific so artistic liberty is encouraged, provided the colors are kept to a minimum and looks consistent with the simple nature of the brand and the matte black packaging.

Also attached an existing beef jerky package with a similar style to what we're looking for.

Industry/Entity Type

It Company

Colors
f59195
ffffff

Requirements
Must have
• Low contrast, flat and minimalist design.
Should not have
• A complicated design with many colors. Gawdy/flashy design. Bright colors. High contrast.

```html
<!DOCTYPE html>
<html lang="en">
<head>
<meta charset="utf-8">
<title>Velmor Beef Jerky – Peppered Pouch</title>
<link rel="stylesheet" href="https://fonts.googleapis.com/css2?family=Antonio:wght@300;400&display=swap">
<style>
  :root {
    --backdrop: #eef0f1;
    --pouch-black: #171717;
    --rose: #f59195;
    --rose-mid: #d9457c;
    --rose-deep: #7a2046;
    --label-red: #ee3b43;
  }
  html, body {
    margin: 0;
    width: 1200px;
    height: 1200px;
    overflow: hidden;
    background: var(--backdrop);
  }
  .canvas {
    position: relative;
    width: 1200px;
    height: 1200px;
  }
  .pouch {
    position: absolute;
    left: 246px;
    top: 114px;
    width: 672px;
    height: 996px;
    background: var(--pouch-black);
    border-radius: 4px 4px 16px 16px;
    overflow: hidden;
  }
  .pouch-art {
    position: absolute;
    inset: 0;
    width: 100%;
    height: 100%;
  }
  .brand {
    position: absolute;
    left: 180px;
    width: 300px;
    top: 162px;
    text-align: center;
    font-family: "Antonio", sans-serif;
    color: var(--rose);
  }
  .brand-name {
    margin: 0;
    font-size: 38px;
    font-weight: 400;
    letter-spacing: 9px;
    line-height: 1;
    padding-left: 9px;
  }
  .brand-tagline {
    margin: 18px 0 0;
    font-size: 25px;
    font-weight: 300;
    letter-spacing: 8px;
    line-height: 1;
    padding-left: 8px;
    color: var(--label-red);
  }
  .product {
    position: absolute;
    right: 212px;
    top: 612px;
    text-align: right;
    font-family: "Antonio", sans-serif;
    font-weight: 300;
    color: var(--label-red);
  }
  .product-name {
    margin: 0;
    font-size: 112px;
    font-weight: 300;
    line-height: 92px;
    letter-spacing: 1px;
  }
  .product-name span { display: block; }
  .product-flavor {
    margin: 10px 0 0;
    font-size: 54px;
    line-height: 48px;
  }
  .product-flavor span {
    display: block;
    font-size: 42px;
    line-height: 38px;
  }
  .net-weight {
    margin: 14px 0 0;
    font-size: 19px;
    font-weight: 400;
    line-height: 19px;
  }
</style>
</head>
<body>
<main class="canvas">
  <article class="pouch">
    <svg class="pouch-art" viewBox="0 0 672 996" role="img" aria-label="Faceted pink bull head illustration in profile, horn sweeping across the top and muzzle across the lower left">
      <defs>
        <linearGradient id="roseSweep" x1="0" y1="0" x2="1" y2="1">
          <stop offset="0" stop-color="#f59195"/>
          <stop offset="0.55" stop-color="#d9457c"/>
          <stop offset="1" stop-color="#7a2046"/>
        </linearGradient>
      </defs>
      <path d="M0 0 H672 V70 C560 90 440 110 300 115 C180 118 80 112 0 104 Z" fill="url(#roseSweep)" opacity="0.85"/>
      <path d="M140 360 L672 340 V560 C520 600 420 640 360 700 L300 760 C250 800 190 830 130 840 L0 850 V560 C70 540 120 470 140 360 Z" fill="url(#roseSweep)" opacity="0.55"/>
    </svg>
    <header class="brand">
      <h1 class="brand-name">VELMOR</h1>
      <p class="brand-tagline">HAND CRAFTED</p>
    </header>
    <section class="product">
      <h2 class="product-name"><span>BEEF</span><span>JERKY</span></h2>
      <p class="product-flavor">PEPPERED<span>FLAVOR</span></p>
      <p class="net-weight">NET WEIGHT<br>3 OZ/100G</p>
    </section>
  </article>
</main>
</body>
</html>
```